Health and Wellness company needs flyer to promote free seminar

Stride reform studio is a health and wellness company that offers an exercise program designed by physical therapists to help relieve pain and improve mobility. Our business is a new concept that is not well understood by the public. In order to promote our business we offer a free seminar where we present information regarding the underlying cause of pain and tightness. During the seminar we also perform a posture screen and movement testing for all participants.

Target Market(s)

Mostly healthy and active women ages 25-65

Industry/Entity Type

Health And Wellness

Font styles to use
Sans Serif

Colors

Designer to choose colors to be used in the design.

Requirements
Must have
• Title: Eliminate Pain and Tightness For Good
• Paragraph: Stride Reform Studio offers a free 60 minute seminar: "The Busy Walker's Handbook to Bending and Standing Taller."
• What to Expect:
• • Identify the underlying cause of your pain and mobility issues
• • Expose what gets in the way of you moving and feeling better
• • Learn why traditional exercises don’t help and can actually make the problem worse
• • Reveal what your posture is saying and how that impacts you
• • Experience your muscle imbalances through movement tests
• • Discover the training method that realigns your posture, increases your mobility and reduces your pain
• Call to action: RSVP online at stridereformstudio.com
Nice to have
• Use a relevant image showing a female dealing with tightness in the low back, legs, etc.
• Emphasize that the seminar is FREE.
• Make the call to action prominent.

```html
<!DOCTYPE html>
<html lang="en">
<head>
<meta charset="utf-8">
<title>Stride Reform Studio – Free Seminar Flyer</title>
<link href="https://fonts.googleapis.com/css2?family=Montserrat:wght@600;700;800;900&family=Lato:ital,wght@0,400;0,700;1,400&family=Kaushan+Script&display=swap" rel="stylesheet">
<style>
  :root{
    --stage:#e6e8ec;
    --paper:#ffffff;
    --paper-soft:#f4f5f6;
    --purple:#5a5fab;
    --orange:#ef8a25;
    --ink:#262626;
    --grey:#8d8d8d;
    --grey-light:#d3d4d6;
    --badge:#454545;
    --photo-a:#c3d0db;
    --photo-b:#e9eef2;
  }
  *{margin:0;padding:0;box-sizing:border-box}
  html,body{width:1200px;height:800px;overflow:hidden;background:var(--stage)}
  .flyer{
    position:absolute;left:330px;top:18px;width:540px;height:764px;
    background:var(--paper);overflow:hidden;
    box-shadow:0 6px 18px rgba(0,0,0,.12);
    font-family:'Lato',sans-serif;color:var(--ink);
  }
  .flyer > svg{position:absolute;left:0;top:0}
  .brand{
    position:absolute;left:232px;top:26px;display:flex;align-items:center;gap:8px;
    font-family:'Montserrat',sans-serif;font-weight:700;font-size:17px;color:var(--purple);
  }
  .brand-square{width:22px;height:22px;background:var(--orange)}
  .headline{
    position:absolute;left:296px;top:168px;
    font-family:'Montserrat',sans-serif;font-weight:900;font-size:31px;line-height:1.02;
    letter-spacing:.5px;
  }
  .headline .hl-purple{color:var(--purple)}
  .headline .hl-grey{color:var(--grey)}
  .headline .hl-orange{color:var(--orange)}
  .headline-rule{position:absolute;left:404px;top:306px;width:110px;height:2px;background:var(--grey)}
  .signup{position:absolute;left:286px;top:338px;width:254px;height:124px}
  .signup-plate{
    position:absolute;left:0;top:0;width:230px;height:124px;background:var(--badge);
    border-radius:4px 4px 30px 30px;
  }
  .signup-title{
    position:absolute;left:16px;top:6px;color:#fff;
    font-family:'Montserrat',sans-serif;font-weight:800;font-size:42px;letter-spacing:1px;
  }
  .signup-band{
    position:absolute;left:8px;top:60px;width:246px;height:28px;background:var(--orange);
    color:#fff;font-family:'Montserrat',sans-serif;font-weight:800;font-size:21px;
    letter-spacing:5px;padding-left:14px;line-height:28px;
  }
  .signup-url{position:absolute;left:18px;top:96px;color:#fff;font-size:12px;letter-spacing:.3px}
  .seminar{position:absolute;right:26px;top:472px;text-align:right}
  .seminar-title{
    font-family:'Montserrat',sans-serif;font-weight:800;font-size:25px;color:#4a4a4a;letter-spacing:.5px;
  }
  .seminar-script{
    font-family:'Kaushan Script',cursive;font-size:27px;line-height:1.1;color:var(--orange);
    margin-top:-4px;margin-right:30px;
  }
  .seminar-intro{
    position:absolute;left:30px;top:446px;width:270px;
    font-size:11.5px;line-height:1.3;color:#444;font-style:italic;
  }
  .seminar-intro strong{color:var(--purple);font-style:normal}
  .expect{
    position:absolute;left:28px;top:500px;width:270px;list-style:none;
    font-size:11px;line-height:1.25;color:#333;
  }
  .expect li{position:relative;padding-left:16px;margin-bottom:3px}
  .expect li::before{
    content:"";position:absolute;left:0;top:3px;
    border-left:8px solid var(--orange);border-top:4px solid transparent;border-bottom:4px solid transparent;
  }
  .expect .lead{color:var(--purple);font-weight:700}
  .contact{
    position:absolute;right:22px;top:648px;color:#fff;
    font-family:'Montserrat',sans-serif;font-weight:700;
  }
  .contact-row{display:flex;align-items:center;gap:8px;justify-content:flex-end;margin-bottom:6px}
  .contact-phone{font-size:18px}
  .contact-web{font-size:13px}
  .contact-icon{width:18px;height:18px}
</style>
</head>
<body>
<main class="flyer">

  <svg class="flyer-shapes" width="540" height="764" viewBox="0 0 540 764" aria-hidden="true">
    <path d="M0,178 C180,168 360,150 540,80 L540,764 L0,764 Z" fill="var(--paper-soft)"/>
    <path d="M0,140 C180,128 380,112 540,38 L540,72 C380,150 180,168 0,178 Z" fill="var(--purple)"/>
    <path d="M0,182 C180,172 370,155 540,84" fill="none" stroke="var(--grey-light)" stroke-width="3"/>
  </svg>

  <svg class="photo" width="540" height="764" viewBox="0 0 540 764" role="img"
       aria-label="Photo of a woman in a white outfit sitting on a mat by a bright window, holding her knee in discomfort">
    <defs>
      <linearGradient id="photoFill" x1="0" y1="0" x2="1" y2="0">
        <stop offset="0" stop-color="var(--photo-a)"/>
        <stop offset=".6" stop-color="var(--photo-b)"/>
        <stop offset="1" stop-color="#ffffff"/>
      </linearGradient>
    </defs>
    <path d="M0,182 C180,172 330,160 420,130 L420,370 C300,420 150,440 0,440 Z" fill="url(#photoFill)"/>
  </svg>

  <svg class="flyer-waves" width="540" height="764" viewBox="0 0 540 764" aria-hidden="true">
    <path d="M300,430 C380,400 440,318 540,290 L540,340 C450,362 400,430 330,444 Z" fill="var(--grey-light)"/>
    <path d="M0,438 C150,438 300,415 420,366 C470,348 510,338 540,334 L540,764 L0,764 Z" fill="var(--paper)"/>
    <path d="M0,438 C150,438 300,415 420,366 C470,348 510,338 540,334" fill="none" stroke="var(--grey-light)" stroke-width="5"/>
    <path d="M540,540 C450,544 396,572 344,634 C324,692 254,740 0,744" fill="none" stroke="var(--grey-light)" stroke-width="3"/>
    <path d="M540,548 C450,552 400,580 350,640 C330,700 260,748 0,752 L0,764 L540,764 Z" fill="var(--orange)"/>
  </svg>

  <div class="brand"><span class="brand-square"></span>Stride Reform Studio</div>

  <h1 class="headline">
    <span class="hl-purple">ELIMINATE</span><br>
    PAIN <span class="hl-grey">AND</span><br>
    TIGHTNESS<br>
    <span class="hl-orange">FOR GOOD</span>
  </h1>
  <div class="headline-rule"></div>

  <div class="signup">
    <div class="signup-plate"></div>
    <div class="signup-title">SIGN UP</div>
    <div class="signup-band">ONLINE AT</div>
    <div class="signup-url">stridereformstudio.com/free-seminar</div>
  </div>

  <div class="seminar">
    <div class="seminar-title">FREE SEMINAR</div>
    <div class="seminar-script">invitation</div>
  </div>

  <p class="seminar-intro"><strong>Stride Reform Studio</strong> offers a free 60 minute seminar: "The Busy Walker's Handbook to Bending and Standing Taller."</p>

  <ul class="expect">
    <li><span class="lead">Identify</span> the underlying cause of your pain and mobility issues</li>
    <li><span class="lead">Expose</span> what gets in the way of you moving and feeling better</li>
    <li><span class="lead">Learn</span> why traditional exercises don't help and can actually make the problem worse</li>
    <li><span class="lead">Reveal</span> what your posture is saying and how that impacts you</li>
    <li><span class="lead">Experience</span> your muscle imbalances through movement tests</li>
    <li><span class="lead">Discover</span> the training method that realigns your posture, increases your mobility and reduces your pain</li>
  </ul>

  <div class="contact">
    <div class="contact-row contact-phone">
      <svg class="contact-icon" viewBox="0 0 24 24" aria-hidden="true"><path d="M6.6 10.8a15 15 0 0 0 6.6 6.6l2.2-2.2a1 1 0 0 1 1-.25 11.4 11.4 0 0 0 3.6.57 1 1 0 0 1 1 1V20a1 1 0 0 1-1 1A17 17 0 0 1 3 4a1 1 0 0 1 1-1h3.5a1 1 0 0 1 1 1c0 1.25.2 2.45.57 3.57a1 1 0 0 1-.25 1z" fill="#fff"/></svg>
      (555) 204-7719
    </div>
    <div class="contact-row contact-web">
      <svg class="contact-icon" viewBox="0 0 24 24" aria-hidden="true"><circle cx="12" cy="12" r="9" fill="none" stroke="#fff" stroke-width="2"/><path d="M3 12h18M12 3c3 3 3 15 0 18M12 3c-3 3-3 15 0 18" fill="none" stroke="#fff" stroke-width="1.6"/></svg>
      stridereformstudio.com
    </div>
  </div>

</main>
</body>
</html>
```